Book Cover Design - Rooted Together: 7 Paths to Raise a Home that Flourishes

International cover needed for the Australian (Marlow Fenwick/QRT Press 2011) non-fiction book Rooted Together: 7 Paths to Raise a Home that Flourishes.

Blurb: With the birth of a baby, come other new beginnings, the birth of a mother, of a father, and of a family. With each stage of a child's growth, and with every new baby, there are more new beginnings. In older cultures and in villages around the world, parenthood was considered a rite of passage but traditions that guided parents into becoming a family have largely been lost - until now.

This ground breaking book walks a new generation of mothers and fathers through the eight steps of the modern parenthood rite of passage, from couple-connection to family-foundations, so they can prepare for and continue to grow a family that thrives.

Bio: Mara Quinlan is a relationship counsellor, parent educator and columnist for Sensible Homelife magazine. She lives in Sydney with her husband, their three gorgeous children and an itinerary of pets. This is her first book.
Updates

Thank you for your patience, I haven't ever done anything like this before and the designs submitted have helped me to be more specific in my requests. Please see the updated brief. The most important point is that I am seeking a TEXT based cover, so BOTH the TITLE and SUBTITLE should take up most of the space, the image could either be in the background with the title and subtitle overlayed, or be much smaller to fit around them. I have attached some more images to the brief, hope they help to convey the 'feel' I am after.  Thanks again!

Reason: Thank you so much for taking an interest in this project, the process has been very educational and helpful for me. While some of the stock art in the submitted designs are great, I've decided to commission a custom illustration which completely captures the meaning of Rooted Together. I will upload the illustration once it's complete for designers who are still interested to use. Thank you for your patience! Mara

Thank you all for your patience and for opening up my thinking about what I am really hoping for with this cover. I have uploaded some new tree designs and more specific instructions that I would like to be included in the cover design. I'm looking forward to seeing your creations!

With warm regards,

Mara

Target Market(s)

Couples thinking about having a baby and new parents of one or more young children.

Industry/Entity Type

Baby

Requirements
Must have
• TEXT based cover with BOTH the TITLE and SUBTITLE taking up most of the page.
Colors to match the Australian version (see attached)
Tree design bottom left (as per Trunk Treatment image attached) OR Heart Tree Design
Root design (as per one of the two images attached)
PLEASE ADD: three new shoots coming up from the ground under the tree to symbolize the children.
Nice to have
• Artistic effect to complement Australian cover.
Subtle retro feel to complement Australian cover.
Should not have
• The book is inclusive of all parents (including same-sex parents) so no images of mother/father and baby.

```html
<!DOCTYPE html>
<html lang="en">
<head>
<meta charset="utf-8">
<title>Rooted Together – Book Cover</title>
<link rel="stylesheet" href="https://fonts.googleapis.com/css2?family=Arimo:wght@400&family=Open+Sans:wght@400&family=Carlito&display=swap">
<style>
  :root {
    --paper: #ffffff;
    --frame: #111111;
    --ink-grey: #6b6b6b;
    --ink-black: #0a0a0a;
    --sky-top: #7cc6e0;
    --sky-low: #cfe9f2;
    --ground: #8a5a26;
  }
  html, body {
    margin: 0;
    padding: 0;
    width: 1200px;
    height: 1000px;
    overflow: hidden;
    background: var(--paper);
  }
  .cover { display: block; width: 1200px; height: 1000px; }
  .cover-frame { fill: var(--paper); stroke: var(--frame); stroke-width: 2; }
  .title-grey { fill: var(--ink-grey); font-family: "Arimo", Arial, sans-serif; }
  .title-black { fill: var(--ink-black); font-family: "Arimo", Arial, sans-serif; }
  .title-accent { fill: var(--ink-black); font-family: "Open Sans", Arial, sans-serif; }
  .author-name { fill: var(--ink-black); font-family: "Carlito", Calibri, sans-serif; font-size: 21px; }
</style>
</head>
<body>
<svg class="cover" viewBox="0 0 1200 1000" xmlns="http://www.w3.org/2000/svg">
  <defs>
    <linearGradient id="landscape-tone" x1="0" y1="0" x2="0" y2="1">
      <stop offset="0" stop-color="var(--sky-top)"/>
      <stop offset="0.55" stop-color="var(--sky-low)"/>
      <stop offset="0.88" stop-color="#d9ecf1"/>
      <stop offset="0.9" stop-color="var(--ground)"/>
      <stop offset="1" stop-color="var(--ground)"/>
    </linearGradient>
  </defs>

  <rect class="cover-frame" x="274.5" y="10.5" width="651" height="977"/>

  <g class="cover-title">
    <text class="title-grey" x="497" y="268" font-size="72" textLength="208" lengthAdjust="spacingAndGlyphs">Rooted</text>
    <text class="title-accent" x="497" y="332" font-size="60" textLength="208" lengthAdjust="spacingAndGlyphs">Together</text>
    <text class="title-grey" x="497" y="400" font-size="62" textLength="208" lengthAdjust="spacingAndGlyphs">7Paths</text>
    <text class="title-grey" x="497" y="457" font-size="38" textLength="40" lengthAdjust="spacingAndGlyphs">to</text>
    <text class="title-black" x="540" y="457" font-size="62" textLength="165" lengthAdjust="spacingAndGlyphs">Raise</text>
    <text class="title-grey" x="497" y="492" font-size="22" textLength="12" lengthAdjust="spacingAndGlyphs">a</text>
    <text class="title-grey" x="511" y="492" font-size="44" textLength="150" lengthAdjust="spacingAndGlyphs">Home</text>
    <text class="title-grey" x="665" y="492" font-size="22" textLength="40" lengthAdjust="spacingAndGlyphs">that</text>
    <text class="title-black" x="497" y="545" font-size="58" textLength="208" lengthAdjust="spacingAndGlyphs">Flourishes</text>
  </g>

  <rect class="cover-illustration" x="497" y="553" width="206" height="227" fill="url(#landscape-tone)" role="img" aria-label="Painted landscape of a lone tree on a grassy hill under a pale blue sky"/>

  <text class="author-name" x="600" y="928" text-anchor="middle">Mara Quinlan</text>
</svg>
</body>
</html>
```